Webdesign for Brisvane for use on webpage

We aim to deliver insights for power consumers in the nordic market in the B2B market, without being a supplier.

Since we are helping customers in the green transition and reducing CO2 emissions, green colors would be preferred, but we are keeping an open mind. We would like to communicate transperancy, awareness and enabling economic potential for customers.

We deliver our product on a SaaS platform through visualization in dashboards

Target Market(s)

B2B

Industry/Entity Type

Power Consumption

Number of Pages Required

1 page

Colors
0054AA
0677BA
7BADD7
CADEEF
E8F1F8
0094D4
00A9DD
6FCCEA
C7EBF8
E9F6FB
00AB8E
00BBA5
67D7C9
C6EFE9
E9F9F6
59FF00
82FF00
B8FF75
E3FFCB
F4FFEA

Requirements
Must have
• The general looks and color schemes must be in line with logo called "brisvane.eps" - see attached

```html
<!DOCTYPE html>
<html lang="en">
<head>
<meta charset="utf-8">
<title>Brisvane – Energy data insights</title>
<link href="https://fonts.googleapis.com/css2?family=DM+Serif+Display&family=Open+Sans:wght@400;600;700;800&display=swap" rel="stylesheet">
<style>
:root{
  --navy:#1d2433;
  --navy-deep:#151b27;
  --blue:#0054AA;
  --blue-mid:#0677BA;
  --blue-light:#7BADD7;
  --green:#59FF00;
  --green-card:#52d90a;
  --green-soft:#E3FFCB;
  --green-pale:#F4FFEA;
  --white:#ffffff;
  --ink:#1d2433;
  --grey:#5d6470;
  --serif:"DM Serif Display", Georgia, serif;
  --sans:"Open Sans", Arial, sans-serif;
}
*{margin:0;padding:0;box-sizing:border-box}
html,body{width:1200px;height:3564px;overflow:hidden}
body{font-family:var(--sans);color:var(--ink);background:var(--white);position:relative}
.btn{display:inline-block;background:var(--blue);color:var(--white);font:600 11px var(--sans);padding:9px 20px;border-radius:4px;text-decoration:none}
.btn-green{background:var(--green);color:var(--navy)}
.brand-name{font:700 18px var(--sans);color:var(--blue)}

/* top bar */
.topbar{position:absolute;top:0;left:0;width:1200px;height:52px;background:var(--navy);display:flex;align-items:center;padding:0 200px}
.topbar .call{color:var(--white);font:700 13px var(--sans)}
.topbar .btn-green{margin-left:70px;border-radius:14px;padding:6px 18px}
.socials{display:flex;gap:6px;margin-left:40px}
.socials span{width:20px;height:20px;border-radius:50%;background:var(--blue)}
.header-brand{position:absolute;right:90px;top:0;width:170px;height:74px;background:var(--white);border-radius:0 0 85px 85px;display:flex;flex-direction:column;align-items:center;justify-content:center;z-index:3}
.header-brand .dot{width:22px;height:22px;border-radius:50%;background:var(--green);margin-bottom:4px}
.header-brand .brand-name{font-size:15px}
/* nav */
.nav{position:absolute;top:52px;left:0;width:1200px;height:22px;background:var(--blue);display:flex;align-items:center;padding-left:200px;gap:28px}
.nav a{color:var(--white);font:600 11px var(--sans);text-decoration:none}

/* hero */
.hero{position:absolute;top:74px;left:0;width:1200px;height:370px;background:linear-gradient(100deg,var(--navy) 55%,#2b3546)}
.hero-brand{position:absolute;left:150px;top:80px;display:flex;flex-direction:column;align-items:center;width:330px}
.hero-brand .disc{width:120px;height:120px;border-radius:50%;background:var(--blue-mid)}
.hero-brand .brand-name{font-size:40px;color:var(--blue-mid);margin-top:16px}
.hero-copy{position:absolute;left:600px;top:40px;width:420px}
.hero-copy h1{font:36px/1.15 var(--serif);color:var(--white)}
.hero-copy p{color:#c9cfda;font-size:11px;line-height:1.6;margin:14px 0 16px;width:270px}
.hero-curve{position:absolute;left:0;bottom:-2px;width:1200px;height:90px}

/* sectors */
.sectors{position:absolute;top:444px;left:0;width:1200px;height:410px;text-align:center}
.section-title{font:38px/1.15 var(--serif);color:var(--ink)}
.sectors .section-title{margin-top:36px}
.cards{display:flex;gap:20px;justify-content:center;margin-top:28px}
.sector-card{width:185px;height:245px;background:var(--blue);color:var(--white);text-align:left;padding:22px 14px;position:relative}
.sector-card.alt{background:var(--green-card)}
.sector-card h3{font:20px/1.1 var(--serif);margin-bottom:12px}
.sector-card p{font-size:9.5px;line-height:1.55}
.sector-card .more{position:absolute;left:14px;bottom:20px;font:600 10px var(--sans)}
.sector-card svg{position:absolute;right:14px;bottom:14px}
.sectors .btn{margin-top:26px;background:var(--navy)}

/* feature */
.feature{position:absolute;top:854px;left:0;width:1200px;height:450px;background:var(--navy)}
.feature .curve-top,.feature .curve-bot{position:absolute;left:0;width:1200px;height:70px}
.feature .curve-top{top:-1px}
.feature .curve-bot{bottom:-1px}
.feature-brand{position:absolute;left:170px;top:95px;width:280px;display:flex;flex-direction:column;align-items:center}
.feature-brand .ring{width:200px;height:200px;border-radius:50%;border:8px solid var(--blue-mid)}
.feature-brand .brand-name{color:var(--green);font-size:22px;margin-top:12px}
.feature-copy{position:absolute;left:610px;top:72px;width:400px;color:var(--white)}
.feature-copy h2{font:36px/1.1 var(--serif)}
.feature-copy p{font-size:10.5px;line-height:1.6;color:#c9cfda;margin-top:10px}
.feature-copy .btn{margin-top:16px}

/* articles */
.articles{position:absolute;top:1312px;left:0;width:1200px;height:540px;text-align:center}
.subtitle{font-size:11px;color:var(--grey);margin-top:6px}
.article-row{position:relative;height:420px;margin-top:26px}
.article{position:absolute;background:var(--white);text-align:left;box-shadow:0 3px 14px rgba(0,0,0,.12)}
.article .photo{width:100%;background:linear-gradient(160deg,#8fb7d8,#4d6f8f 55%,#2d3c4f)}
.article .body{padding:14px}
.article h4{font:13px/1.3 var(--serif)}
.article p{font-size:9px;line-height:1.5;color:var(--grey);margin:8px 0}
.article .more{font:600 10px var(--sans);color:var(--blue)}
.a-left{left:200px;top:40px;width:185px}
.a-left .photo,.a-right .photo{height:150px}
.a-mid{left:430px;top:0;width:340px;z-index:2}
.a-mid .photo{height:230px;background:linear-gradient(165deg,#b9d4ea,#5b86ad 50%,#2f4a66)}
.a-mid .body{text-align:center;padding:18px 40px}
.a-mid h4{font-size:15px}
.a-right{left:815px;top:40px;width:185px}
.articles .btn{position:absolute;left:50%;transform:translateX(-50%);bottom:0;background:var(--navy)}

/* testimonials */
.testimonials{position:absolute;top:1862px;left:0;width:1200px;height:400px;background:var(--blue);text-align:center;color:var(--white)}
.testimonials .curve-top,.testimonials .curve-bot{position:absolute;left:0;width:1200px;height:60px}
.testimonials .curve-top{top:-1px}
.testimonials .curve-bot{bottom:-1px}
.testimonials .section-title{color:var(--white);padding-top:90px}
.quote{width:520px;margin:26px auto 0;font-size:11.5px;line-height:1.7}
.quote-name{font:700 11px var(--sans);margin-top:14px}
.testimonials .btn{background:var(--white);color:var(--navy);margin-top:14px}
.arrow{position:absolute;top:190px}
.arrow.prev{left:190px}.arrow.next{right:190px}

/* quote form */
.quote-form{position:absolute;top:2278px;left:0;width:1200px;height:380px;text-align:center}
.quote-form .section-title{margin-top:30px}
.form{width:730px;margin:30px auto 0;text-align:left}
.form .row{display:flex;gap:18px}
.field{flex:1;height:32px;background:var(--green-pale);border:1px solid #c8e9a8;font-size:9px;color:var(--grey);padding:8px 10px}
.field.area{height:80px;margin-top:16px}
.form .btn{display:block;width:70px;margin:26px auto 0;background:var(--green);color:var(--navy);text-align:center;padding:9px 0}

/* footer */
.footer{position:absolute;top:2675px;left:0;width:1200px;height:889px;background:var(--navy)}
.footer .curve-top{position:absolute;top:-1px;left:0;width:1200px;height:110px}
.footer-brand{position:absolute;left:200px;top:195px;width:200px;display:flex;flex-direction:column;align-items:center}
.footer-brand .dot{width:60px;height:60px;border-radius:50%;background:var(--blue-mid)}
.footer-brand .brand-name{font-size:26px;color:var(--blue-mid);margin-top:10px}
.footer-col{position:absolute;top:180px;color:#c9cfda;font-size:11px;line-height:1.9}
.footer-col h5{font:20px var(--serif);color:var(--green);margin-bottom:10px}
.footer-col .item{display:flex;gap:8px;align-items:flex-start}
.footer-col .item svg{margin-top:4px;flex:none}
.col-contact{left:470px;width:240px}
.col-links{left:790px;width:140px}
.footer-social{position:absolute;left:960px;top:230px;display:flex;flex-direction:column;gap:10px}
.footer-social span{width:22px;height:22px;border-radius:50%;background:var(--blue)}
.copyright{position:absolute;bottom:0;left:0;width:1200px;height:46px;background:var(--navy-deep);color:#9aa3b2;font-size:10px;display:flex;align-items:center;justify-content:center}
</style>
</head>
<body>

<header>
  <div class="topbar">
    <span class="call">Call: 555-014-7720</span>
    <a class="btn btn-green" href="#quote">Get a Free Quote</a>
    <div class="socials"><span></span><span></span><span></span><span></span></div>
  </div>
  <nav class="nav">
    <a href="#">Home</a><a href="#">About Us</a><a href="#">Sectors</a><a href="#">Clients Review</a><a href="#">Blog</a><a href="#">Contact Us</a>
  </nav>
  <div class="header-brand"><span class="dot"></span><span class="brand-name">Brisvane</span></div>
</header>

<section class="hero">
  <div class="hero-brand">
    <span class="disc"></span>
    <span class="brand-name">Brisvane</span>
  </div>
  <div class="hero-copy">
    <h1>We Aim to Deliver Insights for Power Consumers</h1>
    <p>It is a long established fact that a reader will be distracted by the readable content of a page when looking at its layout and calm.</p>
    <a class="btn" href="#">Contact Us</a>
  </div>
  <svg class="hero-curve" viewBox="0 0 1200 90" preserveAspectRatio="none">
    <path d="M0 70 Q600 -10 1200 60 L1200 90 L0 90Z" fill="var(--white)"/>
    <path d="M0 70 Q600 -10 1200 60" fill="none" stroke="var(--green)" stroke-width="6"/>
  </svg>
</section>

<section class="sectors">
  <h2 class="section-title">Discover The Business Sectors of<br>Our Customers</h2>
  <div class="cards">
    <article class="sector-card">
      <h3>Bank &amp;<br>Insurance</h3>
      <p>It is a long established fact that a reader will be distracted by the readable content of a page when looking at its layout.</p>
      <span class="more">Read More →</span>
      <svg width="26" height="26" viewBox="0 0 26 26" fill="none" stroke="#fff" stroke-width="1.5"><path d="M3 10 13 4 23 10M5 11v10M10 11v10M16 11v10M21 11v10M3 23h20"/></svg>
    </article>
    <article class="sector-card alt">
      <h3>Defense &amp;<br>Security</h3>
      <p>It is a long established fact that a reader will be distracted by the readable content of a page when looking at its layout.</p>
      <span class="more">Read More →</span>
      <svg width="26" height="26" viewBox="0 0 26 26" fill="none" stroke="#fff" stroke-width="1.5"><path d="M13 3 22 6v7c0 6-4 9-9 11-5-2-9-5-9-11V6Z"/></svg>
    </article>
    <article class="sector-card">
      <h3>Media &amp;<br>Entertainment</h3>
      <p>It is a long established fact that a reader will be distracted by the readable content of a page when looking at its layout.</p>
      <span class="more">Read More →</span>
      <svg width="26" height="26" viewBox="0 0 26 26" fill="none" stroke="#fff" stroke-width="1.5"><rect x="3" y="6" width="20" height="13"/><path d="M9 23h8M13 19v4"/></svg>
    </article>
    <article class="sector-card">
      <h3>Retail &amp;<br>E-Commerce</h3>
      <p>It is a long established fact that a reader will be distracted by the readable content of a page when looking at its layout.</p>
      <span class="more">Read More →</span>
      <svg width="26" height="26" viewBox="0 0 26 26" fill="none" stroke="#fff" stroke-width="1.5"><path d="M3 4h4l3 13h11l2-9H8"/><circle cx="11" cy="21" r="1.5"/><circle cx="19" cy="21" r="1.5"/></svg>
    </article>
  </div>
  <a class="btn" href="#">View All Sectors</a>
</section>

<section class="feature">
  <svg class="curve-top" viewBox="0 0 1200 70" preserveAspectRatio="none">
    <path d="M0 0 H1200 V20 Q600 80 0 20Z" fill="var(--white)"/>
    <path d="M0 20 Q600 80 1200 20" fill="none" stroke="var(--green)" stroke-width="5"/>
  </svg>
  <div class="feature-brand">
    <span class="ring"></span>
    <span class="brand-name">Brisvane</span>
  </div>
  <div class="feature-copy">
    <h2>Lorem Ipsum is Simply Dummy Text the Printing</h2>
    <p>It is a long established fact that a reader will be distracted by the readable content of a page when looking at its layout. The point of using Lorem Ipsum is that it has a more-or-less normal distribution of letters, as opposed to using content here, making it look like readable English.</p>
    <p>Many desktop publishing packages and web page editors now use Lorem Ipsum as their default model text, and a search will uncover many sites.</p>
    <a class="btn" href="#">Contact Us</a>
  </div>
  <svg class="curve-bot" viewBox="0 0 1200 70" preserveAspectRatio="none">
    <path d="M0 70 V45 Q600 -10 1200 45 V70Z" fill="var(--white)"/>
    <path d="M0 45 Q600 -10 1200 45" fill="none" stroke="var(--green)" stroke-width="5"/>
  </svg>
</section>

<section class="articles">
  <h2 class="section-title">Latest Articles</h2>
  <p class="subtitle">Contrary to popular belief, Lorem Ipsum is not simply random text</p>
  <div class="article-row">
    <article class="article a-left">
      <div class="photo" role="img" aria-label="Photo of a power substation"></div>
      <div class="body">
        <h4>Contrary to Popular Lorem Belief, Lorem Ipsum</h4>
        <p>There are many variations of passages of lorem ipsum available, but the majority have suffered.</p>
        <span class="more">Read More →</span>
      </div>
    </article>
    <article class="article a-mid">
      <div class="photo" role="img" aria-label="Photo of an electricity pylon against the sky"></div>
      <div class="body">
        <h4>Contrary to Popular Lorem Belief, Lorem Ipsum</h4>
        <p>There are many variations of passages of lorem ipsum available, but the majority have suffered alteration.</p>
        <span class="more">Read More →</span>
      </div>
    </article>
    <article class="article a-right">
      <div class="photo" role="img" aria-label="Photo of high-voltage power lines"></div>
      <div class="body">
        <h4>Contrary to Popular Lorem Belief, Lorem Ipsum</h4>
        <p>There are many variations of passages of lorem ipsum available, but the majority have suffered.</p>
        <span class="more">Read More →</span>
      </div>
    </article>
  </div>
  <a class="btn" href="#">View All News</a>
</section>

<section class="testimonials">
  <svg class="curve-top" viewBox="0 0 1200 60" preserveAspectRatio="none">
    <path d="M0 0 H1200 V10 Q600 70 0 35Z" fill="var(--white)"/>
    <path d="M0 35 Q600 70 1200 10" fill="none" stroke="var(--green)" stroke-width="6"/>
  </svg>
  <h2 class="section-title">What Our Clients Say</h2>
  <p class="quote">“ It is a long established fact that a reader will be distracted by the readable content of a page when looking at its layout. The point of using lorem ipsum is that it has a more-or-less normal distribution of letters, as opposed to using content here, content here, making it look like readable English. ”</p>
  <p class="quote-name">Standard Dumb</p>
  <a class="btn" href="#">View All Review</a>
  <svg class="arrow prev" width="14" height="22" viewBox="0 0 14 22"><path d="M12 2 3 11l9 9" fill="none" stroke="#fff" stroke-width="2.5"/></svg>
  <svg class="arrow next" width="14" height="22" viewBox="0 0 14 22"><path d="M2 2l9 9-9 9" fill="none" stroke="#fff" stroke-width="2.5"/></svg>
  <svg class="curve-bot" viewBox="0 0 1200 60" preserveAspectRatio="none">
    <path d="M0 60 V50 Q600 -5 1200 30 V60Z" fill="var(--white)"/>
    <path d="M0 50 Q600 -5 1200 30" fill="none" stroke="var(--green)" stroke-width="6"/>
  </svg>
</section>

<section class="quote-form" id="quote">
  <h2 class="section-title">Get a Free Quote</h2>
  <p class="subtitle">Contrary to popular belief, Lorem Ipsum is not simply random text</p>
  <form class="form">
    <div class="row">
      <div class="field">First Name</div>
      <div class="field">Email</div>
      <div class="field">Phone</div>
    </div>
    <div class="field area">Message</div>
    <span class="btn">Submit</span>
  </form>
</section>

<footer class="footer">
  <svg class="curve-top" viewBox="0 0 1200 110" preserveAspectRatio="none">
    <path d="M0 0 H1200 V20 Q600 140 0 40Z" fill="var(--white)"/>
    <path d="M0 40 Q600 140 1200 20" fill="none" stroke="var(--green)" stroke-width="7"/>
  </svg>
  <div class="footer-brand">
    <span class="dot"></span>
    <span class="brand-name">Brisvane</span>
  </div>
  <div class="footer-col col-contact">
    <h5>Contact Us</h5>
    <div class="item"><svg width="12" height="14" viewBox="0 0 12 14"><path d="M3 1 1 3c0 5 3 9 8 10l2-2-2-3-2 1C5 8 4 7 4 5l1-2Z" fill="var(--green)"/></svg><span>555-014-7720</span></div>
    <div class="item"><svg width="12" height="14" viewBox="0 0 12 14"><path d="M6 1a4 4 0 0 0-4 4c0 3 4 8 4 8s4-5 4-8a4 4 0 0 0-4-4Z" fill="var(--green)"/></svg><span>Fjordvik Park Road, Suite 12<br>Nordhavn 2150</span></div>
    <div class="item"><svg width="12" height="14" viewBox="0 0 12 14"><rect x="1" y="3" width="10" height="8" fill="none" stroke="var(--green)" stroke-width="1.4"/><path d="M1 3l5 4 5-4" fill="none" stroke="var(--green)" stroke-width="1.4"/></svg><span>hello@brisvane-data.com</span></div>
  </div>
  <div class="footer-col col-links">
    <h5>Quick Links</h5>
    Home<br>About Us<br>Sectors<br>Clients Review<br>Blog<br>Contact Us
  </div>
  <div class="footer-social"><span></span><span></span><span></span><span></span></div>
  <div class="copyright">Copyright © 2024 Brisvane | All Rights Reserved</div>
</footer>

</body>
</html>
```